'TOLVANTA' NEW WINE LABEL DESIGN

I am looking for an exceptional and exciting design for a wine label called 'Tolvanta' meaning 'Lookout'. The design must feature the name 'Tolvanta', and the word 'Cabernet Sauvignon' in version 1 and 'Sauvignon Blanc' in version 2. It will also need the words 'Valle Central, Chile' at the bottom of the label as a prominent piece of information as well as the vintage 2017. Please produce the work in size 80mm x 100mm. Feel free to use colour in addition to black/white and ensue that the label is easy to read on a shelf placement.
Target Market(s)
SUPERMARKETS & WINE STORES
Requirements
Must have
- EASY TO READ, USE COLOURS LIKE GREEN FOR SAUVIGNON & RED FOR CABERNET SAUVIGNON
- FULL BOTTLE SHOT MUST BE IN PROVIDED DESIGNS. ALL BOTTLE TOPS SHOULD BE QUORLAN STYLE (SCREW TOP)
- PLEASE NOTE THAT LABEL INFORMATION MUSY BE EASY TO READ I.E. VINTAGE, PLACE OF ORGIN ALTHOUGH NOT THE MAIN CONTENT MUST STILL BE CLEAR.
Nice to have
- ARTISTIC REFERENCE LINK TO NAME & ANDES BUT NOT PICTURES OF MOUNTAINS
Should not have
- PICTURES OF GRAPES
- PICTURES OF VINEYARDS
- PICTURES OF MOUNTAINS

```html
<!DOCTYPE html>
<html lang="en">
<head>
<meta charset="utf-8">
<title>Tolvanta Wine Labels</title>
<link rel="stylesheet" href="https://fonts.googleapis.com/css2?family=Cinzel:wght@600&family=Cormorant+Garamond:wght@500&family=Pinyon+Script&display=swap">
<style>
  :root {
    --backdrop: #a9a9a9;
    --gold: #c9a24a;
    --label-dark: #111111;
    --label-light: #f4f4f2;
    --ink-light: #f1f1f1;
    --ink-dark: #2a2a2a;
    --cabernet-red: #b3121c;
    --sauvignon-green: #2f9a3a;
  }
  * { margin: 0; padding: 0; box-sizing: border-box; }
  html, body { width: 801px; height: 1200px; overflow: hidden; }
  body { background: var(--backdrop); position: relative; }

  .label {
    position: absolute;
    top: 388px;
    width: 340px;
    height: 425px;
    overflow: hidden;
    text-align: center;
    box-shadow: 0 4px 14px rgba(0,0,0,0.25);
  }
  .label--cabernet { left: 40px; background: var(--label-dark); color: var(--ink-light); }
  .label--sauvignon { left: 421px; background: var(--label-light); color: var(--ink-dark); }

  .label__frame {
    position: absolute;
    inset: 10px;
    border: 2px solid var(--gold);
    pointer-events: none;
  }
  .label__ribbon { position: absolute; left: 0; top: 0; }

  .label__crest {
    position: absolute;
    left: 45px;
    top: 30px;
    width: 250px;
    height: 80px;
    border-radius: 40px;
    background: radial-gradient(ellipse at center, #d8b764 0%, #a8843a 55%, rgba(168,132,58,0.15) 100%);
    opacity: 0.85;
  }

  .label__name {
    position: absolute;
    left: 0; right: 0;
    top: 158px;
    font-family: "Cinzel", serif;
    font-weight: 600;
    font-size: 44px;
    letter-spacing: 1px;
    line-height: 1;
  }
  .label--cabernet .label__name { color: var(--gold); }
  .label--sauvignon .label__name { color: var(--sauvignon-green); }

  .label__variety {
    position: absolute;
    left: 0; right: 0;
    top: 256px;
    font-family: "Cormorant Garamond", serif;
    font-weight: 500;
    font-size: 17px;
    letter-spacing: 0.5px;
    line-height: 1;
  }
  .label__vintage {
    position: absolute;
    left: 0; right: 0;
    top: 290px;
    display: flex;
    justify-content: center;
    align-items: center;
    gap: 8px;
    font-family: "Cormorant Garamond", serif;
    font-size: 17px;
    letter-spacing: 1px;
    line-height: 1;
  }
  .label__vintage::before, .label__vintage::after {
    content: "";
    width: 44px;
    height: 1px;
    background: currentColor;
  }
  .label__region {
    position: absolute;
    left: 0; right: 0;
    top: 322px;
    font-family: "Pinyon Script", cursive;
    font-size: 32px;
    line-height: 1;
  }
  .label__country {
    position: absolute;
    left: 0; right: 0;
    top: 372px;
    font-family: "Cormorant Garamond", serif;
    font-size: 16px;
    letter-spacing: 3px;
    line-height: 1;
  }
</style>
</head>
<body>

  <section class="label label--cabernet">
    <svg class="label__ribbon" width="340" height="425" viewBox="0 0 340 425" aria-hidden="true">
      <polygon points="180,413 232,413 328,316 328,268" fill="var(--cabernet-red)"/>
    </svg>
    <div class="label__frame"></div>
    <div class="label__crest" role="img" aria-label="Gold heraldic crest with scrollwork ornament"></div>
    <h1 class="label__name">TOLVANTA</h1>
    <p class="label__variety">CABERNET SAUVIGNON</p>
    <p class="label__vintage">2017</p>
    <p class="label__region">Valle Central</p>
    <p class="label__country">CHILE</p>
  </section>

  <section class="label label--sauvignon">
    <svg class="label__ribbon" width="340" height="425" viewBox="0 0 340 425" aria-hidden="true">
      <polygon points="180,413 232,413 328,316 328,268" fill="var(--sauvignon-green)"/>
    </svg>
    <div class="label__frame"></div>
    <div class="label__crest" role="img" aria-label="Gold heraldic crest with scrollwork ornament"></div>
    <h1 class="label__name">TOLVANTA</h1>
    <p class="label__variety">SAUVIGNON BLANC</p>
    <p class="label__vintage">2017</p>
    <p class="label__region">Valle Central</p>
    <p class="label__country">CHILE</p>
  </section>

</body>
</html>
```